Postcard Design

We are Brightmoor Care. A new way of providing quality healthcare for less. We offer a monthly membership program for $77 per person, $167 per family and cover about 85% of medical conditions. Medical office visits are just $7 each. This innovative program have already saved millions of dollars for it's members in health care costs. We are inviting people to a brief, educational meeting to learn more about how they can save money on their healthcare. We need something catchy and upbeat, positive with 1-2 photos inviting them to come find out more. We will be having appetizers. The date is Wednesday, Feb. 18 drop by between 6-8 pm
Industry/Entity Type
Healthcare

```html
<!DOCTYPE html>
<html lang="en">
<head>
<meta charset="utf-8">
<title>Brightmoor Care – Postcard</title>
<link href="https://fonts.googleapis.com/css2?family=Roboto:wght@700;900&family=Roboto+Condensed:wght@700&display=swap" rel="stylesheet">
<style>
  :root {
    --brand-blue: #1b8bc4;
    --deep-blue: #15609f;
    --navy: #0f4a86;
    --orange: #f07a22;
    --white: #ffffff;
    --photo-light: #dfe7ee;
    --photo-mid: #9fb8cc;
  }
  html, body { margin: 0; padding: 0; overflow: hidden; background: var(--white); }
  .postcard {
    position: relative; width: 1200px; height: 936px; overflow: hidden;
    background: var(--white); font-family: "Roboto", Arial, sans-serif;
  }
  .team-photo {
    position: absolute; left: 428px; top: 0; width: 772px; height: 545px;
    background: linear-gradient(160deg, var(--photo-light) 0%, var(--photo-mid) 55%, #6f95b5 100%);
  }
  .brand {
    position: absolute; left: 60px; top: 70px; display: flex; align-items: center; gap: 16px;
  }
  .brand-dot { width: 34px; height: 34px; border-radius: 50%; background: var(--orange); }
  .brand-name {
    font-weight: 900; font-size: 64px; line-height: 1; color: var(--brand-blue);
  }
  .band { position: absolute; left: 0; top: 0; width: 1200px; height: 936px; }
  .headline {
    position: absolute; left: 40px; top: 468px; width: 450px; margin: 0;
    text-align: center; font-weight: 700; font-size: 62px; line-height: 64px;
    color: var(--white); letter-spacing: 0.5px;
  }
  .headline .accent { color: var(--orange); font-size: 64px; }
  .prices { position: absolute; left: 600px; top: 572px; display: flex; gap: 40px; }
  .price { width: 150px; text-align: center; }
  .price-amount {
    font-family: "Roboto Condensed", "Arial Narrow", sans-serif; font-weight: 700;
    font-size: 68px; line-height: 68px; color: var(--white);
    border-bottom: 3px solid var(--white); padding-bottom: 4px;
  }
  .price-label {
    margin-top: 8px; font-weight: 700; font-size: 20px; line-height: 28px; color: var(--orange);
  }
  .invite {
    position: absolute; left: 0; top: 736px; width: 1058px; height: 96px;
    box-sizing: border-box; padding: 10px 0 0 45px;
    background: var(--orange); border-radius: 0 30px 30px 0;
    color: var(--white); font-weight: 700; font-size: 28px; line-height: 42px;
  }
  .tagline {
    position: absolute; left: 0; top: 878px; width: 1200px; text-align: center;
    font-weight: 700; font-size: 37px; letter-spacing: 1px; color: var(--brand-blue);
  }
  .tagline .sep {
    display: inline-block; width: 14px; height: 14px; border-radius: 50%;
    background: var(--orange); margin: 0 18px; vertical-align: middle;
  }
</style>
</head>
<body>
<div class="postcard">
  <div class="team-photo" role="img" aria-label="Photo of four smiling doctors and nurses in scrubs and white coats with stethoscopes"></div>

  <svg class="band" viewBox="0 0 1200 936" aria-hidden="true">
    <defs>
      <linearGradient id="bandFill" x1="0" y1="0" x2="0" y2="1">
        <stop offset="0" stop-color="#2a9ad2"/>
        <stop offset="1" stop-color="#1762a3"/>
      </linearGradient>
    </defs>
    <path d="M0,440 C300,405 600,440 820,492 C960,525 1100,538 1200,532 L1200,862 L0,862 Z" fill="var(--orange)"/>
    <path d="M0,452 C300,420 600,455 820,506 C960,538 1100,550 1200,545 L1200,862 L0,862 Z" fill="url(#bandFill)"/>
    <rect x="0" y="820" width="1200" height="42" fill="var(--navy)"/>
  </svg>

  <div class="brand">
    <span class="brand-dot"></span>
    <span class="brand-name">Brightmoor<br>Care</span>
  </div>

  <h1 class="headline">JOIN THE<br>HEATHCARE<br><span class="accent">REVOLUTION</span></h1>

  <div class="prices">
    <div class="price"><div class="price-amount">$77</div><div class="price-label">Per Month<br>Individual</div></div>
    <div class="price"><div class="price-amount">$169</div><div class="price-label">Per Month<br>Family</div></div>
    <div class="price"><div class="price-amount">$7</div><div class="price-label">Office<br>Visit</div></div>
  </div>

  <p class="invite" style="margin:0">You are invited to a brief informational meeting to learn how<br>you can save money on your healthcare costs. Details on back.</p>

  <div class="tagline">AFFORDABLE<span class="sep"></span>SIMPLE<span class="sep"></span>REVOLUTIONARY</div>
</div>
</body>
</html>
```